Reel Harbor - Premier Angling Expeditions needs a one of a kind Flyer/Brochure

We need a bold, professional and confident Flyer to help us Brand and advertise what we do for companies and teams.

We Make It Easy for you to Plan Your Next Company Adventure

Reel Harbor specializes in customizing Fishing Adventures for Corporate Teams, Executive Retreats, and VIP Clients.

- Reel Harbor takes care of all the planning, preparation and logistics for all your corporate fishing adventures, so you, and your team can focus on the partnership, create stronger relationships, and enjoy the ever lasting experience these trips have to offer.
- Clients of Reel Harbor get to focus all their energy and attention on the essence of the trip and relationships with your team and leave the details of planning and logistics to Reel Harbor.
- Getting out of the office on trips like these helps create even stronger bonds with your team, customer or clients all while creating lifetime memories.
- All of our services are 100% FREE, and you never pay a dime extra for the trip.
- Service is NOT something we talk about, it's something we provide.
- We help customize the itinerary to create a balanced experience for your entire group
- What you can expect on these adventures: team building, employee retention, stronger partnerships, loyalty, growth of company culture, and good lifelong memories!
- We have Hands-on knowledge of the best Lodges for corporate retreats, team building, or exclusive VIP getaways. No matter the need we have you covered!
- What makes us so Great? There's nothing we don't do for you! We take care of everything from booking the trip, the travel, gear that’s needed, travel insurance, special food requirements, etc. And again, we do all of this for FREE!

"The backbone of our business is service and building strong relationships with our clients, outfitters, and employees….Let our team take care of your team”

Target Market(s)

Business's and Corporations

Font styles to use
Serif
Sans Serif

Colors

Designer to choose colors to be used in the design.

Requirements
Must have
• - Excellent Gammer, and a Creative flow.
• - Contact Info and social media links
• Phone: 208-555-0147
• www.reelharbor-example.com
• FB: www.facebook.com/reelharborexpeditions/
• Instagram: @reelharbor
Nice to have
• I would like the brochure to be either a tri-fold or bi-fold. I will leave that up to the designer.
• I am also up for some new design that I may not know about that looks cool and has a good flow.
Should not have
• Small, or hard to read font.

```html
<!DOCTYPE html>
<html lang="en">
<head>
<meta charset="utf-8">
<title>Reel Harbor - Corporate and VIP Fishing Adventures</title>
<link href="https://fonts.googleapis.com/css2?family=Montserrat:wght@400;600;700&display=swap" rel="stylesheet">
<style>
:root{
  --stage:#e4e1dc;
  --ink:#1f2a33;
  --orange:#e8901a;
  --navy:#0f2a44;
  --navy-deep:#0a1e33;
  --seal:#3d4650;
  --sky-top:#ffffff;
  --sky-bottom:#cfe0f3;
  --sea-1:#6fa6c7;
  --sea-2:#2b6f8f;
  --sea-3:#1c4a5e;
  --white:#ffffff;
}
*{margin:0;padding:0;box-sizing:border-box}
html,body{width:1200px;height:2296px;overflow:hidden}
body{background:var(--stage);font-family:"Montserrat",Arial,sans-serif;color:var(--ink);position:relative}
.flyer{position:absolute;left:40px;top:360px;width:1120px;height:1576px;overflow:hidden;
  background:linear-gradient(180deg,var(--sky-top) 0%,#eaf2fb 35%,var(--sky-bottom) 75%);
  box-shadow:0 10px 30px rgba(0,0,0,.25)}
.testimonials{position:absolute;left:53px;top:62px;width:528px;font-size:16.5px;line-height:23px;text-align:justify;hyphens:auto}
.testimonials p{margin-bottom:23px}
.headline{position:absolute;left:53px;top:376px;width:560px;color:var(--orange);font-weight:700;font-size:24px;line-height:31px;text-transform:uppercase}
.benefits{position:absolute;left:53px;top:458px;width:545px;list-style:none}
.benefits li{position:relative;padding-left:38px;font-weight:700;font-size:15.5px;line-height:20px;margin-bottom:15px;text-align:justify}
.benefits li svg{position:absolute;left:0;top:0;width:21px;height:21px}
.photo{position:absolute;border-radius:22px;border:5px solid var(--white);box-shadow:0 6px 16px rgba(0,0,0,.35)}
.photo-1{left:660px;top:78px;width:340px;height:230px;transform:rotate(6deg);background:linear-gradient(135deg,#7c9a5a,#4d6b3b 55%,#8a8f86)}
.photo-2{left:620px;top:300px;width:360px;height:225px;transform:rotate(-6deg);background:linear-gradient(135deg,#2e3b46,#5d7d6a 50%,#b9c4c9)}
.photo-3{left:690px;top:530px;width:370px;height:270px;transform:rotate(6deg);background:linear-gradient(135deg,#8fa6b8,#51606c 55%,#c9d2d8)}
.sea{position:absolute;left:0;top:1098px;width:1120px;height:478px;
  background:linear-gradient(180deg,var(--sea-1) 0%,var(--sea-2) 35%,var(--sea-3) 100%)}
.angler{position:absolute;left:683px;top:812px;width:376px;height:560px;border-radius:40px 40px 0 0;
  background:linear-gradient(180deg,#6b7f8f 0%,#9bc43a 35%,#6e8f2a 70%,#5a6a55 100%)}
.band{position:absolute;left:0;top:0;width:1120px;height:1576px}
.brand-seal{position:absolute;left:64px;top:1165px;width:325px;height:325px;border-radius:50%;background:var(--seal);
  display:flex;align-items:center;justify-content:center;color:var(--white);font-weight:700;font-size:40px;text-align:center;line-height:46px}
.website{position:absolute;left:91px;top:1512px;color:var(--white);font-size:27px;font-weight:400}
.contact{position:absolute;right:58px;top:1404px;text-align:right;color:var(--white)}
.contact h2{font-weight:400;font-size:28px;margin-bottom:6px}
.contact .phone{color:var(--orange);font-weight:700;font-size:40px;line-height:48px;display:flex;align-items:center;justify-content:flex-end;gap:10px}
.contact .line{color:var(--orange);font-size:16px;line-height:36px;display:flex;align-items:center;justify-content:flex-end;gap:10px}
.contact .line.handle{color:var(--white)}
.contact svg{width:26px;height:26px}
</style>
</head>
<body>
<main class="flyer">
  <section class="testimonials">
    <p>Unbelievable team at reelharbor! Details are the key when planning a trip of a lifetime and these guys have the details dialed. Marcus Vellner Host of Open Water Trails TV Show</p>
    <p>Evan and Reel Harbor are the real deal. They combine excellent customer service with a true understanding of angling travel issues. I just completed a trip to Russia arranged by Evan and Reel Harbor and I would highly recommend their services to anyone! Tom Harlow</p>
    <p>Great company with fantastic people and service! Highly recommend! Lena Corbett Owner of Brightway Travel Studio</p>
  </section>

  <h1 class="headline">Reel Harbor's Corporate and<br>VIP Fishing Adventures</h1>

  <ul class="benefits">
    <li><svg viewBox="0 0 22 22"><circle cx="11" cy="11" r="9.5" fill="none" stroke="#1f2a33" stroke-width="1.8"/><path d="M6.5 11.5l3 3 6-7" fill="none" stroke="#1f2a33" stroke-width="2.2"/></svg>Reel Harbor is a booking agency for fishing adventures around the world.</li>
    <li><svg viewBox="0 0 22 22"><circle cx="11" cy="11" r="9.5" fill="none" stroke="#1f2a33" stroke-width="1.8"/><path d="M6.5 11.5l3 3 6-7" fill="none" stroke="#1f2a33" stroke-width="2.2"/></svg>All of our services are 100% FREE, and you never a dime extra for the trip.</li>
    <li><svg viewBox="0 0 22 22"><circle cx="11" cy="11" r="9.5" fill="none" stroke="#1f2a33" stroke-width="1.8"/><path d="M6.5 11.5l3 3 6-7" fill="none" stroke="#1f2a33" stroke-width="2.2"/></svg>We can customize each trip to fit your specific needs and requirements.</li>
    <li><svg viewBox="0 0 22 22"><circle cx="11" cy="11" r="9.5" fill="none" stroke="#1f2a33" stroke-width="1.8"/><path d="M6.5 11.5l3 3 6-7" fill="none" stroke="#1f2a33" stroke-width="2.2"/></svg>Huge advantage of working with Reel Harbor is that we have access to the best dates, and discounts.</li>
    <li><svg viewBox="0 0 22 22"><circle cx="11" cy="11" r="9.5" fill="none" stroke="#1f2a33" stroke-width="1.8"/><path d="M6.5 11.5l3 3 6-7" fill="none" stroke="#1f2a33" stroke-width="2.2"/></svg>Nobody can beat our prices or deals.</li>
    <li><svg viewBox="0 0 22 22"><circle cx="11" cy="11" r="9.5" fill="none" stroke="#1f2a33" stroke-width="1.8"/><path d="M6.5 11.5l3 3 6-7" fill="none" stroke="#1f2a33" stroke-width="2.2"/></svg>Nobody cares or has more hands-on knowledge of the best lodges.</li>
    <li><svg viewBox="0 0 22 22"><circle cx="11" cy="11" r="9.5" fill="none" stroke="#1f2a33" stroke-width="1.8"/><path d="M6.5 11.5l3 3 6-7" fill="none" stroke="#1f2a33" stroke-width="2.2"/></svg>Lodges roll out the red carpet for our clients</li>
    <li><svg viewBox="0 0 22 22"><circle cx="11" cy="11" r="9.5" fill="none" stroke="#1f2a33" stroke-width="1.8"/><path d="M6.5 11.5l3 3 6-7" fill="none" stroke="#1f2a33" stroke-width="2.2"/></svg>Reel Harbor specializes in the most unique and memorable fishing adventures for corporate teams, and VIP clients.</li>
    <li><svg viewBox="0 0 22 22"><circle cx="11" cy="11" r="9.5" fill="none" stroke="#1f2a33" stroke-width="1.8"/><path d="M6.5 11.5l3 3 6-7" fill="none" stroke="#1f2a33" stroke-width="2.2"/></svg>We create proper expectations, and then exceed form there.</li>
    <li><svg viewBox="0 0 22 22"><circle cx="11" cy="11" r="9.5" fill="none" stroke="#1f2a33" stroke-width="1.8"/><path d="M6.5 11.5l3 3 6-7" fill="none" stroke="#1f2a33" stroke-width="2.2"/></svg>We take care of all the little details; Special food requirements, travel, gear, travel insurance, etc.</li>
    <li><svg viewBox="0 0 22 22"><circle cx="11" cy="11" r="9.5" fill="none" stroke="#1f2a33" stroke-width="1.8"/><path d="M6.5 11.5l3 3 6-7" fill="none" stroke="#1f2a33" stroke-width="2.2"/></svg>We plan so you don't have to.</li>
  </ul>

  <div class="photo photo-1" role="img" aria-label="Two anglers holding a large salmon by a riverbank"></div>
  <div class="photo photo-2" role="img" aria-label="Angler holding a rainbow trout"></div>
  <div class="photo photo-3" role="img" aria-label="Group of anglers on a dock with their catch laid out"></div>

  <div class="sea" role="img" aria-label="Clear ocean water over a rocky seabed under a pale sky"></div>
  <div class="angler" role="img" aria-label="Smiling angler in a green jacket holding a trout over a net"></div>

  <svg class="band" viewBox="0 0 1120 1576" aria-hidden="true">
    <path d="M0 1352 C260 1385 560 1392 800 1360 C920 1343 1030 1320 1120 1302 L1120 1576 L0 1576 Z" fill="#e8901a"/>
    <path d="M0 1366 C260 1400 560 1406 800 1374 C920 1358 1030 1336 1120 1318 L1120 1576 L0 1576 Z" fill="#ffffff"/>
    <path d="M0 1376 C260 1412 560 1418 800 1386 C920 1370 1030 1348 1120 1330 L1120 1576 L0 1576 Z" fill="#0f2a44"/>
    <path d="M0 1500 L1120 1470 L1120 1576 L0 1576 Z" fill="#0a1e33" opacity=".5"/>
  </svg>

  <div class="brand-seal">Reel<br>Harbor</div>
  <p class="website">www.reelharbor-example.com</p>

  <section class="contact">
    <h2>Contact Us</h2>
    <p class="phone">208-555-0147
      <svg viewBox="0 0 26 26"><circle cx="13" cy="13" r="11" fill="none" stroke="#fff" stroke-width="2"/><path d="M9 8c1-1 2 0 2.5 1.5s-1 1.5 0 3 2 2.5 3 2.5 1-1.5 2.5-.5 1.5 2 .5 2.5c-3 2-9-4-8.5-9z" fill="#fff"/></svg>
    </p>
    <p class="line">www.facebook.com/reelharborexpeditions/
      <svg viewBox="0 0 26 26"><circle cx="13" cy="13" r="11" fill="none" stroke="#fff" stroke-width="2"/></svg>
    </p>
    <p class="line handle">@reelharbor
      <svg viewBox="0 0 26 26"><circle cx="13" cy="13" r="11" fill="none" stroke="#fff" stroke-width="2"/></svg>
    </p>
  </section>
</main>
</body>
</html>
```